we need a design for Water Bottle Lable Wrap
The product is called Corvane Water is a restructured water. its a very healthy and rejuvenating water
we were looking at using as a tag ling Restore, Recover, Rejuvenate.

```html
<!DOCTYPE html>
<html lang="en">
<head>
<meta charset="UTF-8">
<title>Corvane Water – Bottle Label Wrap</title>
<link href="https://fonts.googleapis.com/css2?family=Alegreya+Sans:wght@300;400&family=Lato:wght@400&display=swap" rel="stylesheet">
<style>
  :root {
    --page-bg: #e4e6e8;
    --label-bg: #f7f9fb;
    --ink-grey: #5a5f64;
    --ink-navy: #2f5878;
    --ink-tagline: #4a7394;
    --wash-light: rgba(160, 195, 225, 0);
    --wash-mid: #9dbfdc;
    --wash-deep: #5f93c0;
    --wash-teal: #4fb3d6;
    --text-light: #ffffff;
  }
  * { margin: 0; padding: 0; box-sizing: border-box; }
  html, body {
    width: 1200px;
    height: 900px;
    overflow: hidden;
    background: var(--page-bg);
  }
  .canvas {
    position: relative;
    width: 1200px;
    height: 900px;
    display: flex;
    align-items: center;
    justify-content: center;
  }
  .label {
    position: relative;
    width: 640px;
    height: 820px;
    background: var(--label-bg);
    overflow: hidden;
  }
  .label__category {
    position: absolute;
    top: 40px;
    left: 0;
    width: 100%;
    text-align: center;
    font-family: "Lato", sans-serif;
    font-size: 17px;
    letter-spacing: 0.55em;
    color: var(--ink-grey);
  }
  .brand {
    position: absolute;
    top: 250px;
    left: 0;
    width: 100%;
    text-align: center;
  }
  .brand__name {
    font-family: "Alegreya Sans", sans-serif;
    font-weight: 300;
    font-size: 84px;
    line-height: 0.98;
    letter-spacing: 0.02em;
    color: var(--ink-navy);
    text-transform: uppercase;
  }
  .brand__tagline {
    position: absolute;
    top: 440px;
    left: 390px;
    font-family: "Alegreya Sans", sans-serif;
    font-weight: 300;
    font-size: 25px;
    line-height: 1.15;
    color: var(--ink-tagline);
  }
  .wash {
    position: absolute;
    left: 0;
    bottom: 0;
    width: 100%;
    height: 300px;
    background: linear-gradient(to bottom, var(--wash-light) 0%, var(--wash-mid) 40%, var(--wash-deep) 85%, var(--wash-teal) 100%);
  }
  .label__volume {
    position: absolute;
    bottom: 70px;
    left: 0;
    width: 100%;
    text-align: center;
    font-family: "Lato", sans-serif;
    font-size: 26px;
    color: var(--text-light);
  }
</style>
</head>
<body>
  <main class="canvas">
    <section class="label">
      <p class="label__category">RESTRUCTURED WATER</p>
      <div class="brand">
        <h1 class="brand__name">Corvane<br>Water</h1>
      </div>
      <p class="brand__tagline">Restore, Recover,<br>Rejuvenate</p>
      <div class="wash" role="img" aria-label="Soft blue watercolour wave wash along the bottom of the label"></div>
      <p class="label__volume">100ML</p>
    </section>
  </main>
</body>
</html>
```